broucher for electrical contracting buisness

use website template and attached files for colour scheme / ideas

Industry/Entity Type

Electrical

Requirements
Must have
• A5 folded to A4 4 pp format
• use the written content in the broucher word document as a guide

```html
<!DOCTYPE html>
<html lang="en">
<head>
<meta charset="utf-8">
<title>Brennan Electrical – Brochure Cover</title>
<link href="https://fonts.googleapis.com/css2?family=Oswald:wght@700&family=Open+Sans:wght@400;700&display=swap" rel="stylesheet">
<style>
  :root {
    --backdrop: #8e8e8e;
    --navy: #2b2e66;
    --navy-deep: #222555;
    --red: #e13a3b;
    --paper: #ececec;
    --white: #ffffff;
    --ink: #33364f;
    --photo-warm: #c9a77a;
    --photo-light: #e9dcc4;
    --photo-dark: #6b5540;
  }
  * { margin: 0; padding: 0; box-sizing: border-box; }
  html, body { width: 1200px; height: 857px; overflow: hidden; }
  body {
    background: var(--backdrop);
    display: flex;
    align-items: center;
    justify-content: center;
    font-family: "Open Sans", Arial, sans-serif;
  }
  .brochure-cover {
    position: relative;
    width: 552px;
    height: 780px;
    background: var(--paper);
    overflow: hidden;
  }
  .cover-shapes, .cover-photo { position: absolute; inset: 0; width: 100%; height: 100%; }
  .service-list {
    position: absolute;
    top: 24px;
    left: 26px;
    width: 500px;
    font-family: "Oswald", "Arial Narrow", sans-serif;
    font-weight: 700;
    text-transform: uppercase;
    color: var(--navy-deep);
    line-height: 0.9;
  }
  .service-line { display: flex; align-items: baseline; gap: 8px; white-space: nowrap; }
  .service-main { font-size: 62px; }
  .service-side { font-size: 32px; }
  .selling-points {
    position: absolute;
    left: 0;
    top: 632px;
    list-style: none;
  }
  .selling-point {
    display: flex;
    align-items: center;
    gap: 12px;
    height: 26px;
    font-size: 13px;
    color: var(--ink);
  }
  .selling-point::before {
    content: "";
    display: block;
    width: 34px;
    height: 10px;
    background: var(--navy);
  }
  .selling-point:nth-child(even)::before { background: var(--red); }
  .brand {
    position: absolute;
    right: 40px;
    top: 590px;
    display: flex;
    flex-direction: column;
    align-items: center;
    gap: 14px;
  }
  .brand-mark {
    width: 50px;
    height: 50px;
    border-radius: 50%;
    background: var(--red);
  }
  .brand-name {
    font-weight: 700;
    font-size: 24px;
    color: var(--navy);
    letter-spacing: 1px;
    text-transform: uppercase;
    text-align: center;
    line-height: 1.1;
  }
</style>
</head>
<body>
  <main class="brochure-cover">
    <svg class="cover-shapes" viewBox="0 0 552 780" aria-hidden="true">
      <polygon points="0,0 552,0 552,212 0,300" fill="var(--navy)"/>
      <polygon points="0,300 552,212 552,218 0,318" fill="var(--red)"/>
      <polygon points="400,238 552,214 552,230 440,246" fill="var(--white)"/>
      <polygon points="0,565 200,530.6 170,560 0,590" fill="var(--white)"/>
      <polygon points="200,530.6 552,470 552,494 170,560" fill="var(--red)"/>
    </svg>

    <svg class="cover-photo" viewBox="0 0 552 780" role="img" aria-label="Photo of a bright open-plan home interior with pendant lights, kitchen bench and living room">
      <defs>
        <linearGradient id="interior-tones" x1="0" y1="0" x2="1" y2="1">
          <stop offset="0" stop-color="var(--photo-light)"/>
          <stop offset="0.55" stop-color="var(--photo-warm)"/>
          <stop offset="1" stop-color="var(--photo-dark)"/>
        </linearGradient>
      </defs>
      <polygon points="0,318 552,230 552,470 0,565" fill="url(#interior-tones)"/>
    </svg>

    <div class="service-list">
      <div class="service-line"><span class="service-main">Residential</span><span class="service-side">Test Tag</span></div>
      <div class="service-line"><span class="service-main">Industrial</span><span class="service-side">Commercial</span></div>
      <div class="service-line"><span class="service-main">Airconditioning</span></div>
    </div>

    <ul class="selling-points">
      <li class="selling-point">24/7 call outs</li>
      <li class="selling-point">Quality guarantee on all works</li>
      <li class="selling-point">Manufacturer's warranty on all products</li>
      <li class="selling-point">Locally owned and run business</li>
    </ul>

    <div class="brand">
      <div class="brand-mark"></div>
      <div class="brand-name">Brennan<br>Electrical</div>
    </div>
  </main>
</body>
</html>
```